BRV KLN Golf Tournament

Need a flyer/poster design that stands out and intrigues people to attend our golf tournament. Flyer will need to be of print quality, high res, able to be resized as we may use it for a postcard as well. The tournament is held at a 5 star golf course and is of a higher caliber/clientele, mostly male M&A professionals. I would like the flyer to reflect our venue and audience.

Balance of masculine and feminine
More contemporary than conservative
Balance of fun and professional
Bold over traditional

I included two sample flyers that are very different but well done in my opinion.
I prefer multiple uses of fonts, sizes to create visual interest

BRV Pactsmiths logo (this is also tournament name) colors are similar to logo- I like to accent with an aqua because it gives off a clean look
Info: 11th Annual Golf Tournament, Marrowfield Country Club, November 10th
Schedule: Lunch at 11am, Shotgun at noon, Awards Dinner at 5:30pm
Pricing: $175 per player includes one raffle ticket
Register by Wednesday, November 5th www.brvnet-example.org/kln/events
Use the picture of Marrowfield CC if it works
Young Fairways is our charity partner, please use logo
Near bottom, "Sponsorship Opportunities Available"

```html
<!DOCTYPE html>
<html lang="en">
<head>
<meta charset="utf-8">
<title>BRV KLN Golf Tournament – Flyer</title>
<link rel="stylesheet" href="https://fonts.googleapis.com/css2?family=Bungee&family=Oswald:wght@500;600&family=Great+Vibes&display=swap">
<style>
  :root {
    --gold-light: #fbe8b0;
    --gold: #d9b06a;
    --gold-dark: #8a6428;
    --green-head: #6fa332;
    --sky: #9fd3d8;
    --water: #5fa7b0;
    --lawn: #4e8a2a;
    --grass: #3f8a1f;
    --grass-light: #7ac043;
    --band: #eeeeee;
    --band-shade: #c9c9c9;
    --ink: #111111;
    --white: #ffffff;
  }
  * { margin: 0; padding: 0; box-sizing: border-box; }
  html, body { width: 826px; height: 1200px; overflow: hidden; background: #ffffff; }
  .flyer { position: relative; width: 826px; height: 1200px; overflow: hidden; font-family: "Oswald", sans-serif; }

  .course-photo {
    position: absolute; left: 0; top: 0; width: 826px; height: 624px;
    background: linear-gradient(180deg, var(--sky) 0%, #cfe9e6 22%, #7fb56a 40%, var(--lawn) 52%, var(--water) 68%, #3f8c9c 100%);
  }
  .grass-photo {
    position: absolute; left: 0; top: 892px; width: 826px; height: 308px;
    background: linear-gradient(180deg, var(--grass) 0%, var(--grass-light) 55%, var(--grass) 100%);
  }
  .title-band {
    position: absolute; left: 0; top: 620px; width: 826px; height: 274px;
    background: linear-gradient(180deg, var(--band-shade) 0%, var(--band) 8%, var(--white) 50%, var(--band) 92%, var(--band-shade) 100%);
  }

  .frame {
    position: absolute; left: 14px; top: 14px; width: 798px; height: 1172px;
    border: 2px solid rgba(255,255,255,0.85);
  }

  .art { position: absolute; left: 0; top: 0; width: 826px; height: 1200px; }

  .badge {
    position: absolute; left: 333px; top: 128px; width: 160px; height: 116px;
    display: flex; flex-direction: column; align-items: center; justify-content: center; gap: 8px;
  }
  .badge-dot { width: 54px; height: 54px; border-radius: 50%; background: var(--white); border: 3px solid var(--gold); }
  .badge-name { font-family: "Oswald", sans-serif; font-weight: 600; font-size: 20px; color: var(--white); letter-spacing: 1px; }

  .date-seal {
    position: absolute; left: 614px; top: 408px; width: 156px; height: 156px; border-radius: 50%;
    background: radial-gradient(circle at 40% 35%, #ffffff 0%, #eef2f3 60%, #c8d2d6 100%);
    border: 3px solid var(--ink);
    display: flex; flex-direction: column; align-items: center; justify-content: center;
    color: var(--ink); font-family: "Oswald", sans-serif; font-weight: 600; line-height: 1;
  }
  .date-day { font-size: 70px; }
  .date-day sup { font-size: 26px; vertical-align: 34px; margin-left: 2px; }
  .date-month { font-size: 26px; margin-top: 4px; }

  .partner {
    position: absolute; left: 344px; top: 1120px; width: 138px; height: 50px;
    background: var(--white); display: flex; align-items: center; justify-content: center;
    font-family: "Oswald", sans-serif; font-weight: 600; font-size: 17px; color: #1d6fa5;
  }
</style>
</head>
<body>
<main class="flyer">
  <div class="course-photo" role="img" aria-label="Photo of the Marrowfield Country Club clubhouse, flagpoles and a pond with fountains"></div>
  <div class="grass-photo" role="img" aria-label="Close-up photo of fairway grass with a golf ball on a tee"></div>
  <div class="title-band"></div>
  <div class="frame"></div>

  <svg class="art" viewBox="0 0 826 1200" aria-hidden="false">
    <defs>
      <linearGradient id="goldFill" x1="0" y1="0" x2="0" y2="1">
        <stop offset="0" stop-color="#fff3cc"/>
        <stop offset="0.45" stop-color="#e2bd78"/>
        <stop offset="1" stop-color="#a97a34"/>
      </linearGradient>
    </defs>

    <!-- header -->
    <line x1="56" y1="72" x2="190" y2="72" stroke="var(--white)" stroke-width="3"/>
    <line x1="636" y1="72" x2="770" y2="72" stroke="var(--white)" stroke-width="3"/>
    <text class="venue-name" x="413" y="88" text-anchor="middle" textLength="420" lengthAdjust="spacingAndGlyphs"
          font-family="Oswald, sans-serif" font-weight="600" font-size="50" fill="var(--green-head)" stroke="#2d4a12" stroke-width="1">MARROWFIELD COUNTRY CLUB</text>

    <!-- edition -->
    <text class="edition" x="396" y="636" text-anchor="middle" font-family="'Great Vibes', cursive" font-size="170" fill="url(#goldFill)" stroke="var(--gold-dark)" stroke-width="1.5">11th</text>

    <!-- headline -->
    <text class="headline" x="413" y="752" text-anchor="middle" textLength="722" lengthAdjust="spacingAndGlyphs"
          font-family="Bungee, sans-serif" font-size="118" fill="url(#goldFill)" stroke="var(--gold-dark)" stroke-width="2">ANNUAL GOLF</text>
    <text class="headline" x="413" y="874" text-anchor="middle" textLength="630" lengthAdjust="spacingAndGlyphs"
          font-family="Bungee, sans-serif" font-size="118" fill="url(#goldFill)" stroke="var(--gold-dark)" stroke-width="2">TOURNAMENT</text>

    <!-- details -->
    <g font-family="Oswald, sans-serif" font-weight="500" fill="url(#goldFill)" stroke="#3a2a0c" stroke-width="0.8" text-anchor="middle">
      <text x="413" y="938" font-size="30" textLength="610" lengthAdjust="spacingAndGlyphs">LUNCH AT 11AM, SHOTGUN AT NOON, AWARDS DINNER AT 5:30PM</text>
      <text x="413" y="986" font-size="30" textLength="240" lengthAdjust="spacingAndGlyphs">$175 PER PLAYER</text>
      <text x="413" y="1024" font-size="30" textLength="390" lengthAdjust="spacingAndGlyphs">INCLUDES ONE RAFFLE TICKET</text>
      <text x="413" y="1061" font-size="20" textLength="612" lengthAdjust="spacingAndGlyphs">REGISTER BY WEDNESDAY, NOVEMBER 5TH WWW.BRVNET-EXAMPLE.ORG/KLN/EVENTS</text>
      <text x="413" y="1106" font-size="24" textLength="352" lengthAdjust="spacingAndGlyphs">SPONSORSHIP OPPORTUNITIES AVAILABLE</text>
    </g>
  </svg>

  <div class="badge">
    <div class="badge-dot"></div>
    <div class="badge-name">BRV Pactsmiths</div>
  </div>

  <div class="date-seal">
    <div class="date-day">10<sup>TH</sup></div>
    <div class="date-month">NOVEMBER</div>
  </div>

  <div class="partner">Young Fairways</div>
</main>
</body>
</html>
```